Corvella Paintless Dent Removal

Our company works on vehicles removing dents using a highly skilled trade which the metal is massaged out with special tools without disturbing the original paint, hence paintless dent removal. Besides keeping the paint and metal original its also very environmentally friendly since no paint or toxic fillers are used. Also we we are one of the most experienced companies in the business with 25 years

Target Market(s)

Retail Automobile consumers, Auto Dealerships and Auto Body Shops

Industry/Entity Type

Auto Repair

Contact Information for Business Card

Dennis Holbrook
PO Box 538 Ashmere, NY 11952
631-472-8816
corvellapdr@mailnest.example
website corvellapdr.example
youtube corvella paintless dent removal
25 years of experience removing Dents, Dings and Hail Damage

Font styles to use
Serif
Sans Serif

Colors

Designer to choose colors to be used in the design.

Requirements
Must have
• I do like things that are simple but classy and somewhat bold, also I like my logo so that should be somewhat important

```html
<!DOCTYPE html>
<html lang="en">
<head>
<meta charset="utf-8">
<title>Corvella Paintless Dent Removal – Business Card</title>
<link rel="stylesheet" href="https://fonts.googleapis.com/css2?family=Montserrat:wght@500;600;800&display=swap">
<style>
  :root {
    --backdrop: #2b2827;
    --card-top: #ffffff;
    --card-bottom: #e4e4e4;
    --navy: #14284f;
    --green: #7ac943;
    --band-dark: #6f6f6f;
    --band-light: #a9a9a9;
    --ink: #1d1d1d;
  }
  * { box-sizing: border-box; margin: 0; padding: 0; }
  html, body { width: 1200px; height: 716px; overflow: hidden; background: var(--backdrop); }
  body { display: flex; align-items: center; justify-content: center; font-family: "Montserrat", sans-serif; }

  .business-card {
    position: relative;
    width: 1000px; height: 572px;
    background: radial-gradient(ellipse at 55% 30%, var(--card-top) 0%, var(--card-bottom) 90%);
    overflow: hidden;
  }

  .brand {
    position: absolute; left: 300px; top: 90px;
    display: flex; align-items: center; gap: 22px;
  }
  .brand-dot { width: 46px; height: 46px; border-radius: 50%; background: var(--green); flex: none; }
  .brand-name {
    color: var(--navy); font-weight: 800; font-size: 56px; line-height: 1.05;
    letter-spacing: 0.5px;
  }

  .holder-name {
    position: absolute; left: 90px; top: 282px;
    font-weight: 600; font-size: 27px; color: var(--ink);
  }

  .rule-green { position: absolute; left: 0; width: 100%; background: var(--green); }
  .rule-green.top { top: 324px; height: 5px; }
  .rule-green.bottom { top: 520px; height: 26px; }

  .contact-band {
    position: absolute; left: 0; top: 329px; width: 100%; height: 48px;
    background: var(--band-dark);
    display: flex; align-items: center; padding: 0 40px;
    color: #fff; font-weight: 500; font-size: 21px;
  }
  .contact-item { display: flex; align-items: center; gap: 10px; }
  .contact-item svg { width: 22px; height: 22px; flex: none; }
  .divider { width: 2px; height: 48px; background: #4f4f4f; transform: skewX(-30deg); margin: 0 32px; }

  .info-band {
    position: absolute; left: 0; top: 377px; width: 100%; height: 143px;
    background: var(--band-light);
  }
  .channel {
    position: absolute; left: 40px; top: 14px;
    display: flex; align-items: center; gap: 12px;
    font-size: 18px; font-weight: 500; color: var(--ink);
  }
  .channel-mark { width: 18px; height: 18px; background: #d9261c; }
  .tagline {
    position: absolute; right: 40px; top: 30px;
    font-size: 18px; font-weight: 500; color: var(--ink); line-height: 1.45;
  }

  .card-edge { position: absolute; left: 0; top: 546px; width: 100%; height: 26px; background: var(--band-light); }
</style>
</head>
<body>
  <article class="business-card">
    <div class="brand">
      <span class="brand-dot"></span>
      <div class="brand-name">Corvella<br>Paintless Dent Removal</div>
    </div>

    <div class="holder-name">Dennis Holbrook</div>

    <div class="rule-green top"></div>

    <div class="contact-band">
      <div class="contact-item">
        <svg viewBox="0 0 24 24" fill="none" stroke="#7ac943" stroke-width="2"><circle cx="12" cy="12" r="10"/><path d="M2 12h20M12 2c3 3 3 17 0 20M12 2c-3 3-3 17 0 20"/></svg>
        <span>corvellapdr.example</span>
      </div>
      <span class="divider"></span>
      <div class="contact-item">
        <svg viewBox="0 0 24 24" fill="#7ac943"><path d="M6.6 10.8a15 15 0 0 0 6.6 6.6l2.2-2.2a1 1 0 0 1 1-.25 11.4 11.4 0 0 0 3.6.57 1 1 0 0 1 1 1V20a1 1 0 0 1-1 1A17 17 0 0 1 3 4a1 1 0 0 1 1-1h3.5a1 1 0 0 1 1 1c0 1.25.2 2.45.57 3.6a1 1 0 0 1-.25 1z"/></svg>
        <span>631-472-8816</span>
      </div>
      <span class="divider"></span>
      <div class="contact-item">
        <svg viewBox="0 0 24 24" fill="none" stroke="#7ac943" stroke-width="2"><rect x="2" y="5" width="20" height="14"/><path d="M2 5l10 8 10-8"/></svg>
        <span>corvellapdr@mailnest.example</span>
      </div>
    </div>

    <div class="info-band">
      <div class="channel">
        <span class="channel-mark"></span>
        <span>corvella paintless dent removal</span>
      </div>
      <p class="tagline">25 years of experience<br>removing Dents, Dings and Hail Damage</p>
    </div>

    <div class="rule-green bottom"></div>
    <div class="card-edge"></div>
  </article>
</body>
</html>
```